Design required for boutique fire engineering firm in New Zealand

Our website was published based on free Wordpress templates, we'd like something a bit more bespoke, clean and simple.
Updates

Reason: didn't check this finished on a Sunday :)

Target Market(s)

architects, building owners, property developers

Industry/Entity Type

Boutique

Contact Information for Business Card

Logo
Fire Engineering

Desmond Harlow
Principal
+64 21 482 735
desmond@veltrane.nz
veltrane.nz

Number of Pages Required

3 page

Font styles to use
Sans Serif

Requirements
Nice to have
• On the business card, an embossed logo would be great - not sure if that's a design thing or just a print thing?
• Website, existing @ http://veltrane.nz for extent of content and general arrangement that I'm happy with.
• Ability to update the content with project bio's and some photos at a later date would be nice.

```html
<!DOCTYPE html>
<html lang="en">
<head>
<meta charset="utf-8">
<title>Veltrane — Fire Engineering</title>
<link rel="stylesheet" href="https://fonts.googleapis.com/css2?family=Open+Sans:wght@400;600;700&display=swap">
<style>
:root{
  --brand:#17497a;
  --text:#555;
  --dark:#222;
  --panel:#ebebeb;
  --footer:#474747;
  --footer-text:#d6d6d6;
  --white:#fff;
  --dot:#cfcfcf;
}
*{margin:0;padding:0;box-sizing:border-box}
html,body{width:682px;height:1200px;overflow:hidden;background:var(--white)}
body{font-family:"Open Sans",Arial,sans-serif;color:var(--text);position:relative}
.abs{position:absolute}

/* header */
.site-header{position:absolute;left:0;top:0;width:682px;height:62px;background:var(--white)}
.brand{position:absolute;left:75px;top:17px;display:flex;align-items:center;gap:6px}
.brand-mark{width:30px;height:30px;border-radius:50%;background:var(--brand)}
.brand-name{font-size:23px;font-weight:700;color:var(--brand);letter-spacing:-0.3px;line-height:1}
.main-nav{position:absolute;top:30px;font-size:7.3px;color:var(--dark);letter-spacing:.1px}
.main-nav a{position:absolute;white-space:nowrap;color:inherit;text-decoration:none}
.main-nav a.active{color:var(--brand);text-decoration:underline}
.phone{position:absolute;left:529px;top:24px;display:flex;align-items:center;gap:5px;font-size:12px;color:var(--dark)}

/* hero */
.hero{position:absolute;left:0;top:62px;width:682px;height:288px;
  background:radial-gradient(ellipse at 70% 35%,#f9a533 0%,#d76a12 35%,#7a2e06 65%,#1e0c04 100%)}
.hero-title{position:absolute;left:76px;top:132px;color:var(--white);font-weight:700;font-size:21.5px;line-height:1.1}
.hero-sub{position:absolute;left:76px;top:158px;color:var(--white);font-weight:600;font-size:12px}
.hero-arrow{position:absolute;top:135px;width:14px;height:18px;background:rgba(0,0,0,.55)}

/* welcome */
.welcome h1{position:absolute;left:0;width:682px;top:392px;text-align:center;font-size:14.5px;font-weight:600;color:var(--brand)}
.welcome p{position:absolute;left:75px;width:532px;top:414px;text-align:center;font-size:7.1px;line-height:12.8px}

/* feature rows */
.feature{position:absolute;left:0;width:682px;height:182px}
.feature-text{position:absolute;top:0;width:341px;height:182px;background:var(--panel)}
.feature-media{position:absolute;top:0;width:341px;height:182px}
.feature h2{position:absolute;top:33px;font-size:13.6px;font-weight:600;color:var(--brand)}
.feature p{position:absolute;top:58px;width:245px;font-size:6px;line-height:10.9px}
.btn{position:absolute;top:123px;width:54px;height:22px;background:var(--white);font-size:5.8px;color:var(--text);display:flex;align-items:center;justify-content:center}

/* news */
.news h2{position:absolute;left:0;width:682px;top:914px;text-align:center;font-size:13.6px;font-weight:600;color:var(--brand)}
.news-card{position:absolute;top:947px;width:124px;height:123px;background:var(--panel);padding:18px 12px 0 12px}
.news-date{font-size:6.8px;font-weight:700;color:var(--brand);letter-spacing:.1px}
.news-text{margin-top:11px;font-size:8.4px;line-height:12px;color:#333;height:56px}
.news-more{margin-top:6px;font-size:5.6px;text-decoration:underline;color:var(--text)}
.dots{position:absolute;top:1093px;left:318px;display:flex;gap:7px}
.dots span{width:7px;height:7px;border-radius:50%;background:var(--dot)}
.dots span.on{background:var(--brand)}

/* footer */
.site-footer{position:absolute;left:0;top:1145px;width:682px;height:55px;background:var(--footer);color:var(--footer-text);font-size:6px}
.footer-links{position:absolute;left:75px;top:15px;word-spacing:1px}
.copyright{position:absolute;left:75px;top:30px}
.social{position:absolute;left:555px;top:20px;display:flex;gap:5px}
.social span{width:14px;height:14px;border-radius:50%}
</style>
</head>
<body>

<header class="site-header">
  <div class="brand"><span class="brand-mark"></span><span class="brand-name">veltrane</span></div>
  <nav class="main-nav">
    <a class="active" style="left:333px">HOME</a>
    <a style="left:370px">ABOUT US</a>
    <a style="left:421px">SERVICES</a>
    <a style="left:469px">CONTACT US</a>
  </nav>
  <div class="phone">
    <svg width="9" height="9" viewBox="0 0 24 24" aria-hidden="true"><path fill="#222" d="M6.6 10.8a15.1 15.1 0 0 0 6.6 6.6l2.2-2.2c.3-.3.7-.4 1-.2 1.1.4 2.3.6 3.6.6.6 0 1 .4 1 1V20c0 .6-.4 1-1 1A17 17 0 0 1 3 4c0-.6.4-1 1-1h3.5c.6 0 1 .4 1 1 0 1.3.2 2.5.6 3.6.1.3 0 .7-.2 1z"/></svg>
    <span>021 482 735</span>
  </div>
</header>

<section class="hero" role="img" aria-label="Photo of firefighters in silhouette hosing down a large blaze">
  <div class="hero-arrow" style="left:0">
    <svg width="14" height="18" viewBox="0 0 14 18" aria-hidden="true"><path d="M9 4 4 9l5 5" fill="none" stroke="#fff" stroke-width="1"/></svg>
  </div>
  <div class="hero-arrow" style="right:0">
    <svg width="14" height="18" viewBox="0 0 14 18" aria-hidden="true"><path d="M5 4l5 5-5 5" fill="none" stroke="#fff" stroke-width="1"/></svg>
  </div>
  <div class="hero-title">Phasellus nisl est</div>
  <div class="hero-sub">condimentum vitae faucibus</div>
</section>

<section class="welcome">
  <h1>Welcome to Veltrane</h1>
  <p>Veltrane is a boutique fire engineering firm based in Wellington, New Zealand, founded by Desmond Harlow in 2017. We provide consulting services in the built environment, including design and review services to assist in Building Consent applications, advice on property protection matters, observation of construction on site, and regulatory consultation. Desmond has worked as a fire engineer in New Zealand for over 20 years, having graduated from the University of Harrowdale with a Bachelors of Engineering (with Honours) and Masters of Engineering in Fire Engineering, and is a Chartered Professional Engineer.</p>
</section>

<section class="feature" style="top:510px">
  <div class="feature-text" style="left:0">
    <h2 style="left:75px">Our Services</h2>
    <p style="left:75px">Aenean sed quam non sapien faucibus consequat vitae sit amet orci. Praesent quis risus mi. In mollis nulla in pulvinar dictum. Vivamus interdum sagittis felis, ut dapibus ligula feugiat ac. In dictum sapien eu tellus finibus fermentum. Aenean faucibus lacus ut mollis commodo. Donec vestibulum odio sem, ac laoreet massa ullamcorper id.</p>
    <div class="btn" style="left:75px">Read more</div>
  </div>
  <div class="feature-media" style="left:341px;background:linear-gradient(135deg,#ece8e2 0%,#d9d3cb 45%,#c8483f 70%,#b92e27 100%)" role="img" aria-label="Photo of a pump room with red sprinkler pipework and gauges"></div>
</section>

<section class="feature" style="top:692px">
  <div class="feature-media" style="left:0;background:linear-gradient(160deg,#c9cccf 0%,#d8dadc 40%,#b94848 65%,#3a3a3a 100%)" role="img" aria-label="Photo of red sprinkler pipes running along a ceiling beside ducting"></div>
  <div class="feature-text" style="left:341px">
    <h2 style="left:24px">Our Team</h2>
    <p style="left:24px">Aenean sed quam non sapien faucibus consequat vitae sit amet orci. Praesent quis risus mi. In mollis nulla in pulvinar dictum. Vivamus interdum sagittis felis, ut dapibus ligula feugiat ac. In dictum sapien eu tellus finibus fermentum. Aenean faucibus lacus ut mollis commodo. Donec vestibulum odio sem, ac laoreet massa ullamcorper id.</p>
    <div class="btn" style="left:24px">Read more</div>
  </div>
</section>

<section class="news">
  <h2>News</h2>
  <article class="news-card" style="left:75px">
    <div class="news-date">15 NOVEMBER, 2017</div>
    <div class="news-text">Proin porta fermentum ipsum, vel porttitor turpis venenatis luctus volutpat eu sapien.</div>
    <div class="news-more">Read more</div>
  </article>
  <article class="news-card" style="left:211px">
    <div class="news-date">15 NOVEMBER, 2017</div>
    <div class="news-text">Donec sit amet lectus nec mi tempor laoreet ac nec nunc. Duis id auctor sapien</div>
    <div class="news-more">Read more</div>
  </article>
  <article class="news-card" style="left:347px">
    <div class="news-date">15 NOVEMBER, 2017</div>
    <div class="news-text">Nullam accumsan purus vel tempus viverra. Mauris suscipit felis id nunc elementum varius</div>
    <div class="news-more">Read more</div>
  </article>
  <article class="news-card" style="left:483px">
    <div class="news-date">15 NOVEMBER, 2017</div>
    <div class="news-text">Praesent elementum nulla sit amet justo pellentesque scelerisque. Nam et tortor in ante iaculis</div>
    <div class="news-more">Read more</div>
  </article>
  <div class="dots"><span class="on"></span><span></span><span></span><span></span></div>
</section>

<footer class="site-footer">
  <div class="footer-links">Home &nbsp;| &nbsp;About Us &nbsp;| &nbsp;Services &nbsp;| &nbsp;Contact Us</div>
  <div class="copyright">Copyright © 2017 Veltrane. All rights reserved.</div>
  <div class="social">
    <span style="background:#3b5a9a"></span>
    <span style="background:#2aa3e0"></span>
    <span style="background:#1d79b5"></span>
  </div>
</footer>

</body>
</html>
```